Australian Meat, Seafood and Fresh Produce Website

Our organization is looking to design a simple, but eye catching website to show our services.
Our company exports West Australian FRESH fruit and vegetables, seafood and meat.
The website we are looking for would consist of:
- Landing Page
- Company info
- Directors bio
- Page that highlights our products
- Contact us page
We would like it to have a Chinese translated version as well.
Tobin
Target Market(s)
Chinese Market
Industry/Entity Type
It Company
Number of Pages Required
1 page
Look and feel
Each slider illustrates characteristics of the customer's brand and the style your logo design should communicate.

```html
<!DOCTYPE html>
<html lang="en">
<head>
<meta charset="utf-8">
<title>Coralbay Store</title>
<link href="https://fonts.googleapis.com/css2?family=Open+Sans:ital,wght@0,400;0,600;1,400&family=Poiret+One&display=swap" rel="stylesheet">
<style>
:root{
  --dark:#333333;
  --red:#ee2a2a;
  --green:#6b9b14;
  --cream:#eeeee0;
  --text:#222222;
  --muted:#555555;
  --border:#cfcfcf;
  --white:#ffffff;
}
*{margin:0;padding:0;box-sizing:border-box}
html,body{width:777px;height:1200px;overflow:hidden;background:var(--white)}
body{position:relative;font-family:"Open Sans",Arial,sans-serif;color:var(--text)}
.abs{position:absolute}
.display{font-family:"Poiret One","Century Gothic",sans-serif;font-weight:400}

.topbar{left:0;top:0;width:777px;height:30px;background:var(--dark)}
.nav{left:98px;top:0;display:flex;height:30px}
.nav a{display:block;height:30px;line-height:31px;color:#e8e8e8;font-size:9px;text-decoration:none;text-align:center;border-right:1px solid #444}
.nav a.active{background:var(--red);color:var(--white)}
.lang{left:588px;top:0;line-height:31px;color:#e8e8e8;font-size:8px}
.flag{left:637px;top:10px;width:26px;height:12px;background:#ddd;border-radius:1px}
.flag span{position:absolute;left:2px;top:2px;width:13px;height:8px;background:var(--red)}
.flag i{position:absolute;left:18px;top:5px;border:3px solid transparent;border-top-color:#555;border-bottom:0}

.brand{left:0;top:48px;width:777px;display:flex;justify-content:center;align-items:center;gap:8px}
.brand-mark{width:30px;height:30px;border-radius:50%;background:var(--green)}
.brand-name{font-size:22px;color:var(--green);font-weight:400}

.hero{left:99px;top:101px;width:580px;height:213px;border:2px solid #d6d6d6;display:flex;gap:2px;background:#d6d6d6}
.hero div{flex:1}
.tile-meat{background:linear-gradient(160deg,#6a6a6a,#3a3a3a)}
.tile-sea{background:linear-gradient(160deg,#4a4a4a,#8a8a8a 60%,#5a5a5a)}
.tile-fruit{background:linear-gradient(150deg,#b8c84a,#e0472a 35%,#f0a030 60%,#4a8a1c)}
.tile-veg{background:linear-gradient(160deg,#3a3a3a,#6e6e6e 55%,#2e2e2e)}

.section-title{left:0;width:777px;text-align:center;color:#111}
.welcome-title{top:338px;font-size:29px;letter-spacing:1px}
.welcome-copy{left:0;top:373px;width:777px;text-align:center;font-size:8.6px;line-height:14px;color:var(--text)}

.btn{display:block;width:75px;height:21px;line-height:21px;border-radius:11px;color:var(--white);font-size:8.5px;text-align:center;background:var(--green)}
.btn.red{background:var(--red)}

.products{left:0;top:482px;width:777px;height:358px;background:var(--cream)}
.products-title{top:505px;font-size:26px}
.products-sub{left:0;top:537px;width:777px;text-align:center;font-size:8.5px}
.product{top:570px;width:132px}
.product .rule{height:3px;background:var(--green)}
.product .rule.red{background:var(--red)}
.product h3{margin-top:10px;height:20px;text-align:center;font-size:15px;letter-spacing:.5px}
.product .photo{width:132px;height:122px;margin-top:7px}
.product p{margin-top:10px;font-size:7.6px;line-height:11.6px;text-align:justify;text-align-last:justify;height:35px;overflow:hidden}
.product .btn{margin:8px auto 0}
.ph-fruit{background:linear-gradient(140deg,#c0392b,#f39c12 40%,#7cb342 70%,#6d2a4a)}
.ph-veg{background:linear-gradient(150deg,#4a4a4a,#7a7a7a 50%,#3c3c3c)}
.ph-sea{background:linear-gradient(150deg,#9ab0c0,#c8321e 45%,#d7cbb8 80%)}
.ph-meat{background:linear-gradient(150deg,#f2e8e0,#c4202a 35%,#a8151e 65%,#d8b890)}

.newsletter{left:108px;top:868px;width:558px;height:60px;border:1px solid #bdbdbd;background:linear-gradient(90deg,#8a3a1a,#d8582a 30%,#e88a3a 55%,#c93a1e 80%,#7a2a14)}
.newsletter h4{position:absolute;left:10px;top:17px;font-size:20px;color:var(--white)}
.newsletter .field{position:absolute;left:182px;top:18px;width:277px;height:24px;background:var(--white);font-size:7px;font-style:italic;color:#888;line-height:24px;padding-left:8px}
.newsletter .submit{position:absolute;left:459px;top:18px;width:78px;height:24px;background:var(--red);color:var(--white);font-size:9px;text-align:center;line-height:24px}

.director{left:105px;top:947px;width:563px;height:120px;background:var(--cream);border:1px solid var(--border)}
.director .portrait{position:absolute;left:18px;top:16px;width:88px;height:88px;border-radius:50%;border:3px solid var(--white);background:linear-gradient(180deg,#8a8f96,#3c4048);box-shadow:0 0 0 1px #bbb}
.director h4{position:absolute;left:114px;top:23px;font-size:18px;color:#222}
.director p{position:absolute;left:115px;top:46px;width:440px;font-size:7.6px;font-style:italic;line-height:12px;color:#222}
.director .name{position:absolute;left:115px;top:72px;font-size:9px;color:var(--red)}
.director .name small{color:#333;font-size:7px}
.dots{position:absolute;left:518px;top:88px;display:flex;gap:3px}
.dots span{width:6px;height:6px;border-radius:50%;background:#bdbdbd}
.dots span.on{background:var(--green)}

.partner{top:1083px;height:40px;border:1px solid var(--border);text-align:center;line-height:38px;font-size:15px;color:#333;letter-spacing:.5px}
.partner.alt{color:var(--red)}

.footer{left:0;top:1140px;width:777px;height:60px;background:var(--dark)}
.social{left:358px;top:1156px;display:flex;gap:3px}
.social span{width:13px;height:13px;border-radius:50%;border:1px solid #999}
.copyright{left:0;top:1177px;width:777px;text-align:center;font-size:7.5px;color:#ddd}
.copyright b{font-weight:600;color:var(--white)}
</style>
</head>
<body>

<header>
  <div class="abs topbar"></div>
  <nav class="abs nav">
    <a class="active" href="#" style="width:76px">HOME</a>
    <a href="#" style="width:86px">ABOUT US</a>
    <a href="#" style="width:87px">PRODUCTS</a>
    <a href="#" style="width:65px">NEWS</a>
    <a href="#" style="width:92px">CONTACT US</a>
  </nav>
  <div class="abs lang">LANGUAGE :</div>
  <div class="abs flag" role="img" aria-label="Chinese language selector"><span></span><i></i></div>

  <div class="abs brand">
    <span class="brand-mark"></span>
    <span class="brand-name">Coralbay Store</span>
  </div>
</header>

<section class="abs hero">
  <div class="tile-meat" role="img" aria-label="Raw meat cut, greyscale"></div>
  <div class="tile-sea" role="img" aria-label="Lobster and shellfish, greyscale"></div>
  <div class="tile-fruit" role="img" aria-label="Watermelon, pineapple, grapes and bananas"></div>
  <div class="tile-veg" role="img" aria-label="Broccoli and tomatoes, greyscale"></div>
</section>

<section>
  <h1 class="abs section-title display welcome-title">WELCOME</h1>
  <p class="abs welcome-copy">Beciegast nveriti vitaesaert asety kertya aset aplicaboserde nerafae lorem ipsumoditaut. Monsequuntu<br>kerliurase bertasasda buyra sasevar magni dolores eonqui ratione voluptate msequi nesciunt, neque porro quisquamesa dolore nuyfasasertas.<br>Vertyu erauas aitaesa ertyasneo eniptaia desbuays.</p>
  <a class="abs btn" href="#" style="left:351px;top:427px">READ MORE</a>
</section>

<section>
  <div class="abs products"></div>
  <h2 class="abs section-title display products-title">OUR PRODUCTS</h2>
  <p class="abs products-sub">Beciegast nveriti vitaesaert asety kertya aset aplicaboserde nerafae lorem ipsumoditaut. Monsequuntu kerliurase ber tasasda.</p>

  <article class="abs product" style="left:112px">
    <div class="rule"></div>
    <h3 class="display">FRUITS</h3>
    <div class="photo ph-fruit" role="img" aria-label="Assorted fresh fruits"></div>
    <p>Sed ut perspiciatis unde omnis isteghgjk n atus error sit volup tatem accusantium doloreque lauda ntium</p>
    <a class="btn" href="#">READ MORE</a>
  </article>
  <article class="abs product" style="left:252px">
    <div class="rule red"></div>
    <h3 class="display">VEGETABLES</h3>
    <div class="photo ph-veg" role="img" aria-label="Fresh vegetables, greyscale"></div>
    <p>Sed ut perspiciatis unde omnis isteghgjk n atus error sit volup tatem accusantium doloreque lauda ntium</p>
    <a class="btn red" href="#">READ MORE</a>
  </article>
  <article class="abs product" style="left:392px">
    <div class="rule"></div>
    <h3 class="display">SEA FOOD</h3>
    <div class="photo ph-sea" role="img" aria-label="Lobster and shellfish platter"></div>
    <p>Sed ut perspiciatis unde omnis isteghgjk n atus error sit volup tatem accusantium doloreque lauda ntium</p>
    <a class="btn" href="#">READ MORE</a>
  </article>
  <article class="abs product" style="left:532px">
    <div class="rule"></div>
    <h3 class="display">MEAT</h3>
    <div class="photo ph-meat" role="img" aria-label="Raw beef steak on a board"></div>
    <p>Sed ut perspiciatis unde omnis isteghgjk n atus error sit volup tatem accusantium doloreque lauda ntium</p>
    <a class="btn" href="#">READ MORE</a>
  </article>
</section>

<section class="abs newsletter" role="img" aria-label="Newsletter sign-up over a sliced citrus background">
  <h4 class="display">Newsletter Sign Up</h4>
  <div class="field">Enter your E-mail</div>
  <div class="submit">SUBSCRIBE</div>
</section>

<section class="abs director">
  <div class="portrait" role="img" aria-label="Portrait of the company director"></div>
  <h4 class="display">Our Director</h4>
  <p>Sed egestas tincidunt mollis. Suspendisse rhoncus vitae enim et faucibus. Ut dignissim nec arcu nec hendrerit sed arcu odio, sagittis vel diam in, malesuada malesuada risus. Aenean a sem leo.</p>
  <div class="name">Jared Tobin <small>- Manager</small></div>
  <div class="dots"><span class="on"></span><span></span><span class="on"></span><span class="on"></span></div>
</section>

<section>
  <svg class="abs" style="left:108px;top:1098px" width="9" height="12" viewBox="0 0 9 12"><path d="M8 0 L0 6 L8 12Z" fill="#c8c8c8"/></svg>
  <div class="abs partner" style="left:132px;width:118px">Brightmoor</div>
  <div class="abs partner alt" style="left:265px;width:116px">Kestrel</div>
  <div class="abs partner" style="left:397px;width:116px">Brightmoor</div>
  <div class="abs partner" style="left:528px;width:116px">Halvane</div>
  <svg class="abs" style="left:658px;top:1098px" width="9" height="12" viewBox="0 0 9 12"><path d="M1 0 L9 6 L1 12Z" fill="#c8c8c8"/></svg>
</section>

<footer>
  <div class="abs footer"></div>
  <div class="abs social"><span></span><span></span><span></span><span></span></div>
  <p class="abs copyright">2015 © <b>Coralbay Store.</b> All Rights Reserved.</p>
</footer>

</body>
</html>
```